Commercial Refrigeration Service Company requires stylish and fresh looking flyer.

We need a flyer to hand out to new customers. It should have a photo and our branding, list all the services that are offered and our contact details.
We would like two flyers to be supplied, both identical though one offering a discount until July ( Half Price Service Fee ). The flyer should be clear, interesting and in similar colours to the branding package supplied.
Please look at our website for information about the services on offer:
www.frostvale-cooling.com.au

Target Market(s)

Cafes, bars, restaurants, pubs ect.

Font styles to use
Other font styles liked:
• Font package provided

Colors
85cae6
ffffff
333333

Requirements
Must have
• - The photo provided.
• - The company logo.
• - Similar feel to the website & business card.
• - Smooth layout and clear to understand.
Should not have
• - No clunky badges or prints.

```html
<!DOCTYPE html>
<html lang="en">
<head>
<meta charset="utf-8">
<title>Frostvale Commercial Refrigeration Flyer</title>
<link rel="stylesheet" href="https://fonts.googleapis.com/css2?family=Open+Sans:wght@300;400;600;700;800&family=Oswald:wght@500;600;700&family=Great+Vibes&display=swap">
<style>
  :root {
    --sky: #5bc8f0;
    --sky-deep: #2aa7df;
    --navy: #1f4aa0;
    --ink: #333333;
    --dark-ring: #3a3a3c;
    --white: #ffffff;
  }
  html, body { margin: 0; padding: 0; overflow: hidden; background: var(--white); }
  .flyer {
    position: relative; width: 932px; height: 1200px; overflow: hidden;
    background: var(--white); font-family: "Open Sans", sans-serif; color: var(--ink);
  }
  .hero-art { position: absolute; left: 0; top: 0; }
  .headline {
    position: absolute; left: 54px; top: 30px; margin: 0;
    font-family: "Open Sans", sans-serif; font-weight: 700; font-size: 46px;
    line-height: 58px; color: var(--white); letter-spacing: 0.5px;
  }
  .registration {
    position: absolute; left: 180px; top: 504px; margin: 0;
    font-size: 15px; font-weight: 600; line-height: 21px; color: var(--white); letter-spacing: 0.5px;
  }
  .badge {
    position: absolute; left: 599px; top: 414px; width: 190px; height: 190px;
    border-radius: 50%; background: var(--dark-ring);
    display: flex; align-items: center; justify-content: center;
  }
  .badge-inner {
    width: 172px; height: 172px; border-radius: 50%; box-sizing: border-box;
    border: 2px solid var(--sky);
    background: radial-gradient(circle at 50% 40%, #3da6ec, #1a5fc4);
    display: flex; align-items: center; justify-content: center; text-align: center;
    font-weight: 800; font-size: 30px; line-height: 35px; color: var(--white); letter-spacing: -0.5px;
  }
  .intro { position: absolute; left: 54px; top: 620px; width: 440px; font-size: 14.5px; line-height: 19.5px; }
  .intro p { margin: 0 0 10px; }
  .services { position: absolute; left: 54px; top: 810px; margin: 0; padding: 0; list-style: none; }
  .services li {
    display: flex; align-items: center; height: 38.5px;
    font-weight: 700; font-size: 26px; color: #111;
  }
  .services svg { margin-right: 20px; }
  .follow { position: absolute; left: 327px; top: 934px; }
  .follow-label { font-family: "Great Vibes", cursive; font-size: 24px; color: #555; margin: 0 0 8px; }
  .social { display: flex; gap: 10px; }
  .social span { width: 36px; height: 36px; border-radius: 50%; background: var(--navy); display: block; }
  .social span:nth-child(2) { background: var(--ink); }
  .social span:nth-child(3) { background: var(--sky-deep); }
  .brand-box {
    position: absolute; left: 511px; top: 656px; width: 351px; height: 90px;
    background: var(--sky); display: flex; align-items: center; justify-content: center;
    font-weight: 800; font-size: 40px; letter-spacing: 10px; color: var(--ink);
  }
  .contact { position: absolute; left: 471px; width: 440px; top: 808px; text-align: center; }
  .contact-name { margin: 0; font-weight: 300; font-size: 36px; line-height: 44px; color: #555; }
  .contact-phone { margin: 0; font-family: "Oswald", sans-serif; font-weight: 700; font-size: 54px; line-height: 62px; color: var(--ink); }
  .contact-email { margin: 14px 0 0; font-size: 19px; color: var(--ink); letter-spacing: 0.3px; }
  .contact-web { margin: 6px 0 0; font-weight: 600; font-size: 30px; color: var(--navy); }
  .footer-wave { position: absolute; left: 0; top: 990px; }
  .footer-text { position: absolute; right: 62px; top: 1068px; text-align: right; font-family: "Oswald", sans-serif; }
  .footer-text .hours { margin: 0; font-weight: 500; font-size: 33px; line-height: 44px; color: #111; }
  .footer-text .offer { margin: 0; font-weight: 600; font-size: 42px; line-height: 56px; color: var(--white); letter-spacing: 1.5px; }
</style>
</head>
<body>
<main class="flyer">
  <svg class="hero-art" width="932" height="600" viewBox="0 0 932 600">
    <defs>
      <clipPath id="hero-clip">
        <path d="M0,0 H932 V390 C800,445 610,535 410,552 C250,565 110,556 0,540 Z"/>
      </clipPath>
      <linearGradient id="hero-tones" x1="0" y1="0" x2="0" y2="1">
        <stop offset="0" stop-color="#5bc8f0"/>
        <stop offset="0.35" stop-color="#9fd7ee"/>
        <stop offset="0.55" stop-color="#7c8192"/>
        <stop offset="1" stop-color="#4a4d57"/>
      </linearGradient>
    </defs>
    <g clip-path="url(#hero-clip)">
      <rect role="img" aria-label="Photo of a smiling technician in a dark work shirt leaning on a refrigeration service ute with a blue and white canopy" width="932" height="600" fill="url(#hero-tones)"/>
    </g>
    <path d="M0,538 C140,560 300,566 430,552 C620,532 790,452 932,384 V418 C800,482 640,550 450,570 C280,586 120,578 0,560 Z" fill="#1f4aa0"/>
    <path d="M0,560 C130,578 290,586 450,570 C560,560 640,540 700,520 C620,552 520,578 420,584 C260,594 120,586 0,574 Z" fill="#2aa7df"/>
  </svg>

  <h1 class="headline">COMMERCIAL REFRIGERATION<br>&amp; ELECTRICAL SERVICES</h1>
  <p class="registration">ABN: 12 345 678 901<br>Licence No: 400123C</p>

  <div class="badge"><div class="badge-inner">ICE<br>makers<br>&amp; beer<br>systems</div></div>

  <section class="intro">
    <p>Frostvale is completely paperless and uses cloud based trade service software to build a complete profile of your venue and equipment, allowing Dan to offer tailored advice for your business.</p>
    <p>Receive a text message when a technician is on their way and your invoice straight to your email at time of service. Pay with card, cash or cheque on site or online.</p>
  </section>

  <ul class="services">
    <li><svg width="22" height="22" viewBox="0 0 22 22"><circle cx="11" cy="11" r="11" fill="#2aa7df"/><path d="M6,11.5 L9.5,15 L16,7.5" stroke="#fff" stroke-width="2.6" fill="none" stroke-linecap="round" stroke-linejoin="round"/></svg>Commercial Refrigeration</li>
    <li><svg width="22" height="22" viewBox="0 0 22 22"><circle cx="11" cy="11" r="11" fill="#2aa7df"/><path d="M6,11.5 L9.5,15 L16,7.5" stroke="#fff" stroke-width="2.6" fill="none" stroke-linecap="round" stroke-linejoin="round"/></svg>Ice makers</li>
    <li><svg width="22" height="22" viewBox="0 0 22 22"><circle cx="11" cy="11" r="11" fill="#2aa7df"/><path d="M6,11.5 L9.5,15 L16,7.5" stroke="#fff" stroke-width="2.6" fill="none" stroke-linecap="round" stroke-linejoin="round"/></svg>Beer Systems</li>
    <li><svg width="22" height="22" viewBox="0 0 22 22"><circle cx="11" cy="11" r="11" fill="#2aa7df"/><path d="M6,11.5 L9.5,15 L16,7.5" stroke="#fff" stroke-width="2.6" fill="none" stroke-linecap="round" stroke-linejoin="round"/></svg>Electrical</li>
    <li><svg width="22" height="22" viewBox="0 0 22 22"><circle cx="11" cy="11" r="11" fill="#2aa7df"/><path d="M6,11.5 L9.5,15 L16,7.5" stroke="#fff" stroke-width="2.6" fill="none" stroke-linecap="round" stroke-linejoin="round"/></svg>24hr Service</li>
    <li><svg width="22" height="22" viewBox="0 0 22 22"><circle cx="11" cy="11" r="11" fill="#2aa7df"/><path d="M6,11.5 L9.5,15 L16,7.5" stroke="#fff" stroke-width="2.6" fill="none" stroke-linecap="round" stroke-linejoin="round"/></svg>Sales</li>
    <li><svg width="22" height="22" viewBox="0 0 22 22"><circle cx="11" cy="11" r="11" fill="#2aa7df"/><path d="M6,11.5 L9.5,15 L16,7.5" stroke="#fff" stroke-width="2.6" fill="none" stroke-linecap="round" stroke-linejoin="round"/></svg>Installations</li>
  </ul>

  <div class="follow">
    <p class="follow-label">Follow us on:</p>
    <div class="social"><span></span><span></span><span></span></div>
  </div>

  <div class="brand-box">FROSTVALE</div>

  <section class="contact">
    <p class="contact-name">CONTACT: DAN</p>
    <p class="contact-phone">0412 555 019</p>
    <p class="contact-email">info@frostvale-cooling.com.au</p>
    <p class="contact-web">frostvale-cooling.com.au</p>
  </section>

  <svg class="footer-wave" width="932" height="210" viewBox="0 0 932 210">
    <path d="M0,210 V175 C240,90 560,40 932,50 V210 Z" fill="#5bc8f0"/>
    <path d="M0,172 C220,88 540,28 932,36 V70 C620,52 320,92 0,200 Z" fill="#1f4aa0"/>
    <path d="M360,60 C560,30 760,26 932,30 V36 C760,30 560,36 360,60 Z" fill="#5bc8f0"/>
  </svg>

  <div class="footer-text">
    <p class="hours">24 HR SERVICE</p>
    <p class="offer">SALES &amp; INSTALLATIONS</p>
  </div>
</main>
</body>
</html>
```